Greta Polanski Consulting

I am starting my own business and want to have a business card that stands out from the rest. Class is the word i use to describe what i would like to my card to look like.

I see my card as vibrant red card with rounded edges. mat finish
Centered scripted writing
large scripted font: Greta Polanski, smaller font & not scripted: Consulting, next line 0438157226, next line greta@polanskihome.com.au

i have now left 2 email message for the design of my card. Family is spelt wrong on the card. this needs to be correct and finial proof sent though!!! before i can download and approve
Greta

Target Market(s)

Real Estate Professionals

Industry/Entity Type

Business

Contact Information for Business Card

Greta Polanski
Consulting
0438 157 226
greta@polanskihome.com.au

Logo Text

no logo

Requirements
Must have
• must have rounded edges

```html
<!DOCTYPE html>
<html lang="en">
<head>
<meta charset="utf-8">
<title>Greta Polanski Consulting – Business Card</title>
<link rel="stylesheet" href="https://fonts.googleapis.com/css2?family=Pacifico&family=Poppins:wght@600&family=Roboto:wght@300&family=Questrial&display=swap">
<style>
  :root {
    --card-red: #ea3237;
    --ink-white: #ffffff;
    --page-bg: #ffffff;
  }
  html, body {
    margin: 0;
    padding: 0;
    width: 980px;
    height: 1200px;
    overflow: hidden;
    background: var(--page-bg);
  }
  .canvas {
    position: relative;
    width: 980px;
    height: 1200px;
  }
  .business-card {
    position: absolute;
    left: 79px;
    top: 378px;
    width: 822px;
    height: 444px;
    background: var(--card-red);
    border-radius: 46px;
    color: var(--ink-white);
    text-align: center;
  }
  .card-name {
    position: absolute;
    left: 0;
    right: 0;
    top: 92px;
    margin: 0;
    font-family: "Pacifico", cursive;
    font-weight: 400;
    font-size: 68px;
    line-height: 1;
    letter-spacing: 0.5px;
  }
  .card-title {
    position: absolute;
    left: 0;
    right: 0;
    top: 226px;
    margin: 0;
    font-family: "Poppins", sans-serif;
    font-weight: 600;
    font-size: 46px;
    line-height: 1;
  }
  .card-phone {
    position: absolute;
    left: 0;
    right: 0;
    top: 297px;
    margin: 0;
    font-family: "Roboto", sans-serif;
    font-weight: 300;
    font-size: 32px;
    line-height: 1;
    letter-spacing: 1px;
  }
  .card-email {
    position: absolute;
    left: 0;
    right: 0;
    top: 336px;
    margin: 0;
    font-family: "Questrial", sans-serif;
    font-size: 30px;
    line-height: 1;
  }
</style>
</head>
<body>
  <main class="canvas">
    <section class="business-card" aria-label="Business card front">
      <h1 class="card-name">Greta Polanski</h1>
      <p class="card-title">Consulting</p>
      <p class="card-phone">0438157226</p>
      <p class="card-email">greta@polanskihome.com.au</p>
    </section>
  </main>
</body>
</html>
```